Website redesign for job agency recruitment

Please refer to the attached document, “Meridale Work Portal Outline,” for comprehensive details regarding the scope, objectives, and requirements of this website redesign project.

For imagery you can use images from this website https://www.pixaboreal.com or any other you regularly use.

Target Market(s)

Jobseekers and Companies looking for general labour

Industry/Entity Type

Services: Oil, Gas and Mining, Administrative, Construction and Trades, Warehouse and Logistics and, Manufacturing.

Number of Pages Required

5+ page

Font styles to use
Serif
Other font styles liked:
• Inter, Open-Sans or similar.

Requirements
Must have
• The requirements highlighted in the Word document attached. The final design needs to be provided in Figma including all viewports (Desktop, mobiel and tablet)
Should not have
• Website we like as a reference: www.quillvanestaffing.com, www.bexistaffing.com, www.zupran.com, www.fennickstaffing.com, www.7tpersonnel.com, www.hiringonthetrail.ca

```html
<!DOCTYPE html>
<html lang="en">
<head>
<meta charset="utf-8">
<title>Meridale Work Agency – Home and About Us</title>
<link href="https://fonts.googleapis.com/css2?family=Poppins:wght@300;400;500;600&family=Inter:wght@400;500;600&display=swap" rel="stylesheet">
<style>
:root{
  --board:#9dc2f2;
  --navy:#0d3c97;
  --navy-deep:#072a70;
  --yellow:#f6c107;
  --ink:#151a2c;
  --muted:#5b6172;
  --soft-blue:#eef4fc;
  --soft-yellow:#fff8e3;
  --footer:#070a24;
  --line:#dde4ef;
  --white:#ffffff;
}
*{margin:0;padding:0;box-sizing:border-box}
html,body{width:700px;height:1200px;overflow:hidden;background:var(--board)}
body{font-family:"Poppins",sans-serif;color:var(--ink)}
.board{position:absolute;left:0;top:0;width:1470px;height:2520px;transform:scale(0.47619);transform-origin:0 0;background:var(--board)}
.board-label{position:absolute;top:42px;font:300 23px "Poppins",sans-serif;letter-spacing:6px;color:var(--white);text-align:center;width:631px}
.page{position:absolute;background:var(--white);overflow:hidden}
.abs{position:absolute}
.ph{position:absolute}
.nav{position:absolute;top:30px;left:317px;font:500 6.5px "Inter",sans-serif}
.nav span{position:absolute;white-space:nowrap}
.brand{position:absolute;left:40px;top:24px;display:flex;align-items:center;gap:5px;font:600 8px "Poppins",sans-serif;width:90px;line-height:1.2}
.brand i{display:block;width:14px;height:14px;border-radius:50%;flex:none}
.eyebrow{font:500 6px "Inter",sans-serif;letter-spacing:1.3px;color:var(--navy);text-transform:uppercase}
.lead{font:400 8px/1.45 "Poppins",sans-serif;color:var(--ink)}
.body{font:300 7.6px/1.45 "Poppins",sans-serif;color:var(--muted)}
.btn{position:absolute;display:flex;align-items:center;justify-content:center;gap:5px;font:400 8px "Poppins",sans-serif;border-radius:2px}
.btn svg{width:6px;height:6px}
.btn-yellow{background:var(--yellow);color:var(--ink)}
.btn-navy{background:var(--navy);color:var(--white)}
.btn-white{background:var(--white);color:var(--ink)}
.section-title{font:400 15px "Poppins",sans-serif;color:var(--navy);text-align:center}
.center{text-align:center}
.service{position:absolute;width:116px;height:170px;background:var(--white);border:1px solid var(--line);border-radius:3px;box-shadow:0 2px 6px rgba(13,60,151,.12);text-align:center;padding:10px 7px 0}
.service h4{font:400 8.5px/1.25 "Poppins",sans-serif;color:var(--ink)}
.service p{font:300 5.8px/1.4 "Poppins",sans-serif;color:var(--muted);margin-top:3px}
.service .ph{left:8px;right:8px;bottom:8px;height:86px;border-radius:2px}
.service .more{position:absolute;left:0;right:0;bottom:16px;font:400 7.5px "Poppins",sans-serif;color:var(--white);text-align:center}
.feature{position:absolute;width:100px;text-align:center}
.feature .ico{width:30px;height:30px;margin:0 auto;background:var(--navy);border-radius:3px;display:flex;align-items:center;justify-content:center}
.feature h5{font:400 8.5px "Poppins",sans-serif;margin-top:14px}
.feature p{font:300 6px/1.45 "Poppins",sans-serif;color:var(--ink);margin-top:5px}
.step{position:absolute;left:360px;width:150px}
.step b{font:500 8px "Poppins",sans-serif;color:var(--navy)}
.step b span{font-size:9.5px;margin-right:5px}
.step p{font:300 5.6px/1.45 "Poppins",sans-serif;color:var(--muted);margin-top:4px}
.jobs{position:absolute;left:0;width:631px;height:235px}
.job{position:absolute;top:57px;width:125px;height:130px;background:#fafafa;border:1px solid var(--line);border-radius:3px;padding:10px}
.job .logo-box{position:absolute;left:10px;top:10px;width:19px;height:19px;border-radius:3px}
.job .co{position:absolute;left:35px;top:11px;font:600 6px "Inter",sans-serif}
.job .type{position:absolute;left:35px;top:22px;font:400 4.5px "Inter",sans-serif;color:#9aa0ad}
.job .role{position:absolute;left:10px;top:42px;font:500 6px "Inter",sans-serif;color:var(--navy)}
.job .pay{position:absolute;left:10px;top:51px;font:400 4.3px "Inter",sans-serif;color:var(--ink)}
.job .desc{position:absolute;left:10px;top:67px;width:105px;font:400 4.5px/1.6 "Inter",sans-serif;color:#a3a8b3}
.job .tags{position:absolute;left:10px;top:100px;display:flex;gap:4px}
.job .tags span{font:400 3.8px "Inter",sans-serif;color:var(--muted);background:#eceef2;border-radius:2px;padding:3px 7px}
.testi{position:absolute;left:0;width:631px;height:258px}
.testi h3{position:absolute;left:128px;top:0;font:400 15px "Poppins",sans-serif}
.testi .sub{position:absolute;left:128px;top:22px;width:170px;font:300 7.6px/1.4 "Poppins",sans-serif}
.see-all{position:absolute;left:463px;top:17px;width:40px;height:19px;font:500 4.5px "Inter",sans-serif;border-radius:2px}
.review{position:absolute;width:95px}
.review .stars{color:var(--yellow);font-size:7px;letter-spacing:1px}
.review p{font:400 4.6px/1.6 "Inter",sans-serif;color:var(--muted);margin-top:5px}
.review b{display:block;font:600 5.5px "Inter",sans-serif;margin-top:8px}
.review small{display:block;font:400 3.8px "Inter",sans-serif;color:#9aa0ad;margin-top:3px}
.footer{position:absolute;left:0;width:631px;height:181px;background:var(--footer);color:var(--white)}
.footer .f{position:absolute;font:400 6px/1.6 "Inter",sans-serif;color:#d6d9e6}
.footer .ft{position:absolute;font:500 7px "Inter",sans-serif;color:var(--white)}
.footer .social{position:absolute;left:65px;top:103px;display:flex;gap:17px}
.footer .social i{display:block;width:8px;height:8px;border-radius:50%;background:var(--yellow)}
.footer .rule{position:absolute;left:52px;right:52px;top:147px;height:1px;background:#2a2e4a}
.footer .copy{position:absolute;left:0;right:0;top:162px;text-align:center;font:400 5px "Inter",sans-serif;color:#c8cbd9}
.value{position:absolute;width:102px;height:78px;border-radius:3px;text-align:center;padding-top:10px}
.value h6{font:600 5.6px "Inter",sans-serif;margin-top:5px}
.value p{font:400 5px/1.45 "Inter",sans-serif;color:var(--muted);margin:4px 10px 0}
.v-blue{background:var(--soft-blue)}
.v-yellow{background:var(--soft-yellow)}
</style>
</head>
<body>
<div class="board">

  <div class="board-label" style="left:90px">HOME PAGE</div>
  <div class="board-label" style="left:749px">ABOUT US PAGE</div>

  <main class="page home" style="left:90px;top:83px;width:631px;height:2354px">

    <section class="hero abs" style="left:0;top:0;width:631px;height:355px">
      <div class="ph" role="img" aria-label="Upward view of glass skyscrapers against a deep blue sky with warm sunset reflections" style="inset:0;background:radial-gradient(ellipse at 45% 100%,#b8532a 0%,#5a2140 25%,transparent 55%),linear-gradient(180deg,#0a1a6a 0%,#0b1548 45%,#140c28 100%)"></div>
      <div class="brand" style="color:var(--white)"><i style="background:var(--yellow)"></i>Meridale Work Agency Ltd.</div>
      <nav class="nav" style="left:0;color:var(--white)">
        <span style="left:317px">Home</span><span style="left:355px">Candidates</span><span style="left:411px">Companies</span><span style="left:466px">About Us</span><span style="left:513px">Contact</span><span style="left:558px">Forms &amp; Links</span>
      </nav>
      <div class="abs center" style="left:0;width:631px;top:117px;color:var(--white)">
        <div style="font:300 19px 'Poppins',sans-serif">Our Goal Is</div>
        <div style="font:500 24px 'Poppins',sans-serif;margin-top:-2px">Your Success</div>
        <div style="font:300 9px/1.35 'Poppins',sans-serif;margin-top:4px">Meridale Work Agency Offer Various<br>Opportunities In The Different Industries.</div>
      </div>
      <div class="btn btn-yellow" style="left:212px;top:216px;width:100px;height:21px">For Candidates</div>
      <div class="btn btn-white" style="left:319px;top:216px;width:99px;height:21px">For Employers</div>
    </section>

    <section class="what-we-do">
      <div class="ph" role="img" aria-label="Smiling young woman in a white t-shirt holding a laptop and cheering" style="left:92px;top:385px;width:196px;height:202px;background:radial-gradient(ellipse at 50% 45%,#d9c4b3 0%,#eef0f4 55%,#ffffff 75%)"></div>
      <div class="abs eyebrow" style="left:324px;top:407px">What we do</div>
      <p class="abs lead" style="left:324px;top:420px;width:200px">Meridale Work Agency offers a complete range of staffing services to keep pace with your career or operational demands.</p>
      <p class="abs body" style="left:324px;top:462px;width:205px">We understand it's not only daunting but very costly in both time &amp; money to make your business thrive in a rapidly changing environment.</p>
      <div class="btn btn-yellow" style="left:324px;top:512px;width:75px;height:21px">Apply Here <svg viewBox="0 0 10 10"><path d="M2 8 8 2M3 2h5v5" stroke="currentColor" stroke-width="1.4" fill="none"/></svg></div>
    </section>

    <section class="how-it-works abs" style="left:0;top:587px;width:631px;height:188px;background:var(--soft-blue)">
      <div class="abs eyebrow" style="left:127px;top:33px">How it works</div>
      <p class="abs lead" style="left:127px;top:45px;width:200px">Lorem ipsum dolor sit amet, consectetur adipiscing elit. Donec quis suscipit nisi. Maecenas tincidunt cursus nibh, at venenatis lectus.</p>
      <p class="abs body" style="left:127px;top:85px;width:195px">Donec rutrum arcu sit amet sem tempus, nec feugiat erat porta. Curabitur dictum tellus nec dui scelerisque consectetur. Aliquam et eros odio.</p>
      <div class="btn btn-navy" style="left:127px;top:133px;width:75px;height:20px">Apply Here <svg viewBox="0 0 10 10"><path d="M2 8 8 2M3 2h5v5" stroke="currentColor" stroke-width="1.4" fill="none"/></svg></div>
      <div class="abs" style="left:341px;top:33px;width:1px;height:125px;background:#9aa6bd"></div>
      <div class="step" style="top:32px"><b><span>01</span>Explore Opportunities</b><p>Dapibus sagittis porta lorem nibh consequat nibh diam id pharetra velit urna magna</p></div>
      <div class="step" style="top:77px"><b><span>02</span>Apply with Ease</b><p>Dapibus sagittis porta lorem nibh consequat nibh diam id pharetra velit urna magna</p></div>
      <div class="step" style="top:121px"><b><span>03</span>Connect and Thrive</b><p>Dapibus sagittis porta lorem nibh consequat nibh diam id pharetra velit urna magna</p></div>
    </section>

    <section class="services">
      <svg class="abs" style="left:150px;top:770px" width="330" height="90" viewBox="0 0 330 90">
        <path d="M10 5 Q40 80 165 82 Q290 80 320 5" stroke="#d4e3f7" stroke-width="3" fill="none"/>
        <circle cx="40" cy="43" r="7" fill="#fff" stroke="#8fa4c8" stroke-width="1"/>
        <circle cx="123" cy="80" r="7" fill="var(--yellow)"/>
        <circle cx="207" cy="80" r="7" fill="#fff" stroke="#8fa4c8" stroke-width="1"/>
        <circle cx="290" cy="43" r="7" fill="#fff" stroke="#f2dc8a" stroke-width="1"/>
      </svg>
      <h2 class="abs section-title" style="left:0;width:631px;top:804px">Services</h2>

      <article class="service" style="left:67px;top:860px;border-color:#b7c4da">
        <h4>Oil, Gas &amp; Mining</h4>
        <p>We are Oil, Gas &amp; Mining Staffing Advisors – Digging Deeper!</p>
        <div class="ph" role="img" aria-label="Miner in hard hat on an industrial drilling rig" style="background:linear-gradient(160deg,#7fa1c8,#4a5a6e 60%,#2b3038)"></div>
        <div class="more">Read More ↗</div>
      </article>
      <article class="service" style="left:194px;top:883px;border-color:#f2dc8a">
        <h4>Administrative</h4>
        <p>We are Administrative Staffing Advisors –Efficiency, Reliability, Accountability</p>
        <div class="ph" role="img" aria-label="Office worker reviewing documents at a desk" style="background:linear-gradient(160deg,#c9ccd2,#6a6d72 60%,#303236)"></div>
        <div class="more">Read More ↗</div>
      </article>
      <article class="service" style="left:321px;top:883px;border-color:#9fb3d8">
        <h4>Construction<br>&amp; Trades</h4>
        <p>We are Construction Staffing Advisors – A Gold Seal is not a Can of Tuna!</p>
        <div class="ph" role="img" aria-label="City skyline with cranes over buildings under construction" style="background:linear-gradient(180deg,#5d95c2,#3d6f96 55%,#2a3a4a)"></div>
        <div class="more">Read More ↗</div>
      </article>
      <article class="service" style="left:448px;top:860px;border-color:#f2dc8a">
        <h4>Warehouse<br>&amp; Logistics</h4>
        <p>We are Warehouse &amp; Logistics Staffing Advisors – Time, Service and Budget</p>
        <div class="ph" role="img" aria-label="Warehouse aisle with tall shelving stacked with boxes" style="background:linear-gradient(160deg,#3f6fa3,#b8733a 55%,#4d3a2c)"></div>
        <div class="more">Read More ↗</div>
      </article>
    </section>

    <section class="features">
      <div class="abs eyebrow center" style="left:0;width:631px;top:1092px">Lorem ipsum</div>
      <p class="abs lead center" style="left:165px;width:300px;top:1104px">Vivamus sed lacinia tellus. Integer a tortor suscipit, mattis risus vel, rhoncus purus. Cras sit amet nibh sit amet est lacinia egestas non vitae turpis.</p>
      <p class="abs body center" style="left:190px;width:250px;top:1136px">Donec rutrum arcu sit amet sem tempus, nec feugiat erat porta. Curabitur dictum tellus nec dui scelerisque consectetur. Aliquam et eros odio.</p>
      <div class="feature" style="left:94px;top:1190px"><div class="ico"><svg width="16" height="16" viewBox="0 0 16 16" fill="none" stroke="#fff" stroke-width="1.2"><rect x="3" y="2" width="10" height="7" rx="1"/><path d="M5 14l3-5 3 5"/></svg></div><h5>Lorem Ipsum</h5><p>Lorem ipsum dolor sit amet, consectetur adipiscing elit. Donec quis suscipit nisi, Maecenas tincidunt mcursus nibh.</p></div>
      <div class="feature" style="left:208px;top:1190px"><div class="ico"><svg width="16" height="16" viewBox="0 0 16 16" fill="none" stroke="#fff" stroke-width="1.2"><circle cx="8" cy="8" r="5"/><circle cx="8" cy="8" r="2"/></svg></div><h5>Lorem Ipsum</h5><p>Lorem ipsum dolor sit amet, consectetur adipiscing elit. Donec quis suscipit nisi, Maecenas tincidunt mcursus nibh.</p></div>
      <div class="feature" style="left:322px;top:1190px"><div class="ico"><svg width="16" height="16" viewBox="0 0 16 16" fill="none" stroke="#fff" stroke-width="1.2"><circle cx="7" cy="7" r="4"/><path d="M10 10l4 4"/></svg></div><h5>Lorem Ipsum</h5><p>Lorem ipsum dolor sit amet, consectetur adipiscing elit. Donec quis suscipit nisi, Maecenas tincidunt mcursus nibh.</p></div>
      <div class="feature" style="left:437px;top:1190px"><div class="ico"><svg width="16" height="16" viewBox="0 0 16 16" fill="none" stroke="#fff" stroke-width="1.2"><rect x="2" y="3" width="12" height="8" rx="1"/><path d="M4 9l3-3 2 2 3-3M8 11v3"/></svg></div><h5>Lorem Ipsum</h5><p>Lorem ipsum dolor sit amet, consectetur adipiscing elit. Donec quis suscipit nisi, Maecenas tincidunt mcursus nibh.</p></div>
    </section>

    <section class="band abs" style="left:0;top:1366px;width:631px;height:211px;background:var(--navy)">
      <div class="abs eyebrow" style="left:67px;top:41px;color:#cfd9ee">How it works</div>
      <p class="abs lead" style="left:67px;top:53px;width:200px;color:var(--white)">Lorem ipsum dolor sit amet, consectetur adipiscing elit. Donec quis suscipit nisi. Maecenas tincidunt cursus nibh, at venenatis lectus.</p>
      <p class="abs body" style="left:67px;top:93px;width:200px;color:#e4eaf6">Donec rutrum arcu sit amet sem tempus, nec feugiat erat porta. Curabitur dictum tellus nec dui scelerisque consectetur. Aliquam et eros odio.</p>
      <div class="btn btn-yellow" style="left:67px;top:141px;width:75px;height:20px">Apply Here <svg viewBox="0 0 10 10"><path d="M2 8 8 2M3 2h5v5" stroke="currentColor" stroke-width="1.4" fill="none"/></svg></div>
      <div class="ph" role="img" aria-label="Smiling construction worker in a yellow hard hat holding a tablet" style="left:262px;top:20px;width:170px;height:191px;background:radial-gradient(ellipse at 50% 55%,#4f6ea8 0%,#2a4f9a 60%,transparent 80%)"></div>
    </section>
    <div class="ph" role="img" aria-label="Business team meeting around a laptop in a bright office" style="left:421px;top:1352px;width:144px;height:114px;background:linear-gradient(135deg,#e7ecf1,#9aa7b5 55%,#4c5560)"></div>
    <div class="ph" role="img" aria-label="Business team meeting around a laptop in a bright office" style="left:421px;top:1476px;width:144px;height:114px;background:linear-gradient(135deg,#e7ecf1,#9aa7b5 55%,#4c5560)"></div>

    <section class="jobs" style="top:1625px">
      <h2 class="abs section-title" style="left:0;width:631px;top:0">Latest Featured Jobs</h2>
      <p class="abs body center" style="left:195px;width:240px;top:26px;color:var(--ink)">Donec rutrum arcu sit amet sem tempus, nec feugiat erat porta. Curabitur dictum tellus nec aliquam et eros odio.</p>
      <article class="job" style="left:120px;width:135px"><div class="logo-box" style="background:#131a4a"></div><div class="co">Brightcode Inc.</div><div class="type">Full-time Worker</div><div class="role">Software Engineer</div><div class="pay">Salary: $80,000 per year</div><div class="desc">Nunc sed libero sollicitudin faucibus. Aliquam viverra maecenas amet ut porta aliquam nunc morbi.</div><div class="tags"><span>Lorem Ipsum</span><span>Lorem Ipsum</span><span>Lorem Ipsum</span></div></article>
      <article class="job" style="left:263px;width:119px"><div class="logo-box" style="background:#131a4a"></div><div class="co">Carewell Ltd.</div><div class="type">Full-time Worker</div><div class="role">Registered Nurse</div><div class="pay">Salary: $60,000 - $80,000 per year</div><div class="desc">Nunc sed libero sollicitudin faucibus. Aliquam viverra maecenas amet ut porta aliquam nunc morbi.</div><div class="tags"><span>Lorem Ipsum</span><span>Lorem Ipsum</span></div></article>
      <article class="job" style="left:391px;width:119px;background:var(--white)"><div class="logo-box" style="background:#131a4a"></div><div class="co">Learnpath Corp</div><div class="type" style="color:var(--ink)">Full-time Worker</div><div class="role">English Teacher</div><div class="pay">Salary: $40,000 - $50,000 per year</div><div class="desc" style="color:var(--ink)">Nunc sed libero sollicitudin faucibus. Aliquam viverra maecenas amet ut porta aliquam nunc morbi.</div><div class="tags"><span>Lorem Ipsum</span><span>Lorem Ipsum</span></div></article>
      <div class="btn btn-yellow" style="left:286px;top:211px;width:58px;height:20px">Button <svg viewBox="0 0 10 10"><path d="M2 8 8 2M3 2h5v5" stroke="currentColor" stroke-width="1.4" fill="none"/></svg></div>
    </section>

    <section class="testi" style="top:1915px">
      <h3>Testimonials</h3>
      <p class="sub">Donec rutrum arcu sit amet sem tempus, nec feugiat erat porta, curabitur dictum.</p>
      <div class="btn btn-navy see-all">SEE ALL</div>
      <div class="abs" style="left:126px;top:199px;width:22px;height:30px;background:var(--navy)"></div>
      <div class="abs" style="left:232px;top:118px;width:28px;height:30px;background:var(--yellow)"></div>
      <div class="ph" role="img" aria-label="Confident businesswoman in a grey blazer with arms crossed" style="left:138px;top:70px;width:108px;height:188px;background:radial-gradient(ellipse at 50% 60%,#8aa0bd 0%,#c9d3df 55%,#ffffff 80%)"></div>
      <div class="review" style="left:292px;top:73px"><div class="stars">★★★★★</div><p>Sed placerat convallis aenean fermentum. Aliquet eget feugiat sed consectetur sodales eleifend.</p><b>Mara Quill</b><small>Marketing Manager</small></div>
      <div class="review" style="left:407px;top:73px"><div class="stars">★★★★★</div><p>Sed placerat convallis aenean fermentum. Aliquet eget feugiat sed consectetur sodales eleifend.</p><b>Tessa Rowan</b><small>Marketing Manager</small></div>
      <div class="review" style="left:292px;top:160px"><div class="stars">★★★★★</div><p>Sed placerat convallis aenean fermentum. Aliquet eget feugiat sed consectetur sodales eleifend.</p><b>Joan Pell</b><small>Marketing Manager</small></div>
      <div class="review" style="left:407px;top:160px"><div class="stars">★★★★★</div><p>Sed placerat convallis aenean fermentum. Aliquet eget feugiat sed consectetur sodales eleifend.</p><b>Owen Brisk</b><small>Marketing Manager</small></div>
    </section>

    <footer class="footer" style="top:2173px">
      <div class="ft" style="left:65px;top:36px">Meridale Work Agency Ltd.</div>
      <p class="f" style="left:65px;top:55px;width:135px;font-size:5.5px">Penatibus congue ipsum condimentum ac dignissim non mi auctor. Nulla id id non enim venenatis nibh. Nunc erat morbi auctor.</p>
      <div class="social"><i></i><i></i><i></i><i></i></div>
      <div class="ft" style="left:312px;top:36px;font-weight:400;font-size:8px">Contact</div>
      <p class="f" style="left:312px;top:56px">Toronto, Vancouver,<br>Calgary</p>
      <p class="f" style="left:312px;top:82px">1-888-555-0142</p>
      <p class="f" style="left:312px;top:95px">support@meridalework.com</p>
      <p class="f" style="left:422px;top:36px;line-height:20px">Home<br>About Us<br>Services<br>Events</p>
      <p class="f" style="left:473px;top:36px;line-height:20px">Customer Support<br>How It Works<br>Terms &amp; Condition<br>Privacy Policy</p>
      <div class="rule"></div>
      <div class="copy">© Meridale Work Agency Ltd. | All rights reserved 2024</div>
    </footer>
  </main>

  <main class="page about" style="left:749px;top:83px;width:631px;height:1696px">

    <header class="about-hero abs" style="left:0;top:0;width:631px;height:308px">
      <div class="brand" style="color:var(--navy);top:22px"><i style="background:var(--yellow)"></i>Meridale Work Agency Ltd.</div>
      <nav class="nav" style="left:0;color:var(--ink)">
        <span style="left:318px">Home</span><span style="left:355px">Candidates</span><span style="left:411px">Companies</span><span style="left:466px">About Us</span><span style="left:513px">Contact</span><span style="left:558px">Forms &amp; Links</span>
      </nav>
      <div class="abs" style="left:43px;top:117px">
        <div style="font:300 19px 'Poppins',sans-serif">Lorem Ipsum</div>
        <div style="font:500 24px 'Poppins',sans-serif;margin-top:-3px">Lorem Ipsum</div>
        <p style="font:300 9px/1.35 'Poppins',sans-serif;width:195px;margin-top:4px">Lorem Ipsum Dolor Sit Amet, Consectetur Adipiscing Elit. Donec Vel Faucibus Leo, Sed Vulputate Risus.</p>
      </div>
      <div class="btn btn-yellow" style="left:43px;top:230px;width:99px;height:21px">For Candidates</div>
      <div class="btn btn-navy" style="left:150px;top:230px;width:99px;height:21px">For Employers</div>
      <div class="ph" role="img" aria-label="Businesswoman and businessman standing back to back in suits" style="left:318px;top:80px;width:180px;height:228px;background:radial-gradient(ellipse at 50% 60%,#6b6e78 0%,#c9ccd2 50%,#ffffff 78%)"></div>
      <div class="abs" style="left:301px;top:138px;width:22px;height:22px;background:var(--navy);border-radius:3px;display:flex;align-items:center;justify-content:center"><svg width="10" height="10" viewBox="0 0 10 10"><path d="M2 4h2l4-2v6L4 6H2z" fill="#fff"/></svg></div>
      <div class="abs" style="left:481px;top:148px;width:90px;height:65px;background:#f6f8fc;border-radius:4px;box-shadow:0 2px 6px rgba(13,60,151,.1);font:300 7px/1.35 'Poppins',sans-serif;text-align:center;padding:10px 8px">Lorem ipsum dolor sit amet, consec tetur adipis asugb cing elit.</div>
      <div class="abs" style="left:547px;top:242px;width:23px;height:22px;background:var(--yellow);border-radius:3px;display:flex;align-items:center;justify-content:center"><svg width="12" height="8" viewBox="0 0 12 8"><rect x="0.5" y="0.5" width="11" height="7" rx="2" fill="#131a4a"/></svg></div>
    </header>

    <section class="intro-band abs center" style="left:0;top:308px;width:631px;height:91px;background:var(--navy);color:var(--white)">
      <p style="font:400 7.6px/1.45 'Poppins',sans-serif;width:280px;margin:19px auto 0">Meridale Work Agency offers a complete range of staffing services to keep pace with your career or operational demands.</p>
      <p style="font:300 7.6px/1.45 'Poppins',sans-serif;width:300px;margin:6px auto 0">Donec rutrum arcu sit amet sem tempus, nec feugiat erat porta. Curabitur dictum tellus nec dui scelerisque consectetur. Aliquam et eros odio.</p>
    </section>

    <section class="values">
      <div class="abs eyebrow center" style="left:0;width:631px;top:441px">Empowering success</div>
      <h2 class="abs center" style="left:0;width:631px;top:458px;font:400 15px 'Poppins',sans-serif">Partnering in the Journey of <span style="color:var(--navy)">2,000</span> Thriving Enterprises</h2>
      <p class="abs body center" style="left:165px;width:300px;top:485px;color:var(--ink)">Donec rutrum arcu sit amet sem tempus, nec feugiat erat porta. Curabitur dictum tellus nec dui scelerisque consectetur. Aliquam et eros odio.</p>

      <div class="value v-blue" style="left:155px;top:532px"><svg width="12" height="12" viewBox="0 0 12 12" fill="none" stroke="var(--navy)"><circle cx="6" cy="6" r="5"/><circle cx="6" cy="6" r="2.5"/><circle cx="6" cy="6" r=".6" fill="var(--navy)"/></svg><h6>Integrity</h6><p>Enim nascetur mauris mi enim feugiat nec turpis feugiat.</p></div>
      <div class="value v-yellow" style="left:265px;top:532px"><svg width="12" height="12" viewBox="0 0 12 12" fill="none" stroke="var(--navy)"><path d="M1 5l10-4-4 10-1.5-4.5z"/></svg><h6>Innovation</h6><p>Enim nascetur mauris mi enim feugiat nec turpis feugiat.</p></div>
      <div class="value v-blue" style="left:375px;top:532px"><svg width="12" height="12" viewBox="0 0 12 12" fill="none" stroke="var(--navy)"><path d="M6 1l1.5 3.2 3.5.4-2.6 2.4.7 3.5L6 8.8 2.9 10.5l.7-3.5L1 4.6l3.5-.4z"/></svg><h6>Empowerment</h6><p>Enim nascetur mauris mi enim feugiat nec turpis feugiat.</p></div>
      <div class="value v-yellow" style="left:155px;top:617px"><svg width="12" height="12" viewBox="0 0 12 12" fill="none" stroke="var(--navy)"><path d="M6 1l5 2.5-5 2.5-5-2.5zM1 6l5 2.5L11 6M1 8.5L6 11l5-2.5"/></svg><h6>Diversity and Inclusion</h6><p>Enim nascetur mauris mi enim feugiat nec turpis feugiat.</p></div>
      <div class="value v-blue" style="left:265px;top:617px"><svg width="12" height="12" viewBox="0 0 12 12" fill="none" stroke="var(--navy)"><circle cx="6.5" cy="6" r="4.5"/><path d="M1 6h1.5"/></svg><h6>Customer-Centricity</h6><p>Enim nascetur mauris mi enim feugiat nec turpis feugiat.</p></div>
      <div class="value v-yellow" style="left:375px;top:617px"><svg width="12" height="12" viewBox="0 0 12 12" fill="none" stroke="var(--navy)"><circle cx="6" cy="4" r="2.2"/><path d="M2 11c0-2.5 1.8-4 4-4s4 1.5 4 4"/></svg><h6>Collaboration</h6><p>Enim nascetur mauris mi enim feugiat nec turpis feugiat.</p></div>
    </section>

    <section class="about-how">
      <div class="ph" role="img" aria-label="Colleagues gathered around a laptop in a modern glass office" style="left:99px;top:739px;width:195px;height:166px;background:linear-gradient(135deg,#e7ecf1,#9aa7b5 55%,#4c5560)"></div>
      <div class="abs" style="left:76px;top:858px;width:89px;height:62px;background:var(--navy);border-radius:3px;color:var(--white);font:300 7px/1.35 'Poppins',sans-serif;text-align:center;padding:8px 6px">Lorem ipsum dolor sit amet, consec tetur adipis asugb cing elit.</div>
      <div class="abs eyebrow" style="left:318px;top:755px">How it works</div>
      <p class="abs lead" style="left:318px;top:767px;width:200px">Lorem ipsum dolor sit amet, consectetur adipiscing elit. Donec quis suscipit nisi. Maecenas tincidunt cursus nibh, at venenatis lectus.</p>
      <p class="abs body" style="left:318px;top:805px;width:200px">Donec rutrum arcu sit amet sem tempus, nec feugiat erat porta. Curabitur dictum tellus nec dui scelerisque consectetur. Aliquam et eros odio.</p>
      <div class="abs" style="left:318px;top:852px;width:13px;height:13px;background:var(--navy);border-radius:2px"></div>
      <p class="abs body" style="left:318px;top:871px;width:105px;font-size:6.3px;color:var(--ink)">Donec rutrum arcu sit amet sem tempus, nec feugiat erat.</p>
      <div class="abs" style="left:426px;top:850px;width:1px;height:42px;background:var(--line)"></div>
      <div class="abs" style="left:436px;top:852px;width:13px;height:13px;background:var(--navy);border-radius:2px"></div>
      <p class="abs body" style="left:436px;top:871px;width:105px;font-size:6.3px;color:var(--ink)">Donec rutrum arcu sit amet sem tempus, nec feugiat erat.</p>
    </section>

    <section class="jobs" style="top:967px">
      <h2 class="abs section-title" style="left:0;width:631px;top:0">Latest Featured Jobs</h2>
      <p class="abs body center" style="left:195px;width:240px;top:26px;color:var(--ink)">Donec rutrum arcu sit amet sem tempus, nec feugiat erat porta. Curabitur dictum tellus nec aliquam et eros odio.</p>
      <article class="job" style="left:120px;width:135px"><div class="logo-box" style="background:#131a4a"></div><div class="co">Brightcode Inc.</div><div class="type">Full-time Worker</div><div class="role">Software Engineer</div><div class="pay">Salary: $80,000 per year</div><div class="desc">Nunc sed libero sollicitudin faucibus. Aliquam viverra maecenas amet ut porta aliquam nunc morbi.</div><div class="tags"><span>Lorem Ipsum</span><span>Lorem Ipsum</span><span>Lorem Ipsum</span></div></article>
      <article class="job" style="left:263px;width:119px"><div class="logo-box" style="background:#131a4a"></div><div class="co">Carewell Ltd.</div><div class="type">Full-time Worker</div><div class="role">Registered Nurse</div><div class="pay">Salary: $60,000 - $80,000 per year</div><div class="desc">Nunc sed libero sollicitudin faucibus. Aliquam viverra maecenas amet ut porta aliquam nunc morbi.</div><div class="tags"><span>Lorem Ipsum</span><span>Lorem Ipsum</span></div></article>
      <article class="job" style="left:391px;width:119px;background:var(--white)"><div class="logo-box" style="background:#131a4a"></div><div class="co">Learnpath Corp</div><div class="type" style="color:var(--ink)">Full-time Worker</div><div class="role">English Teacher</div><div class="pay">Salary: $40,000 - $50,000 per year</div><div class="desc" style="color:var(--ink)">Nunc sed libero sollicitudin faucibus. Aliquam viverra maecenas amet ut porta aliquam nunc morbi.</div><div class="tags"><span>Lorem Ipsum</span><span>Lorem Ipsum</span></div></article>
      <div class="btn btn-yellow" style="left:287px;top:222px;width:57px;height:20px">Button <svg viewBox="0 0 10 10"><path d="M2 8 8 2M3 2h5v5" stroke="currentColor" stroke-width="1.4" fill="none"/></svg></div>
    </section>

    <section class="testi" style="top:1258px">
      <h3>Testimonials</h3>
      <p class="sub">Donec rutrum arcu sit amet sem tempus, nec feugiat erat porta, curabitur dictum.</p>
      <div class="btn btn-navy see-all">SEE ALL</div>
      <div class="abs" style="left:126px;top:199px;width:22px;height:30px;background:var(--navy)"></div>
      <div class="abs" style="left:232px;top:118px;width:28px;height:30px;background:var(--yellow)"></div>
      <div class="ph" role="img" aria-label="Confident businesswoman in a grey blazer with arms crossed" style="left:138px;top:70px;width:108px;height:188px;background:radial-gradient(ellipse at 50% 60%,#8aa0bd 0%,#c9d3df 55%,#ffffff 80%)"></div>
      <div class="review" style="left:292px;top:73px"><div class="stars">★★★★★</div><p>Sed placerat convallis aenean fermentum. Aliquet eget feugiat sed consectetur sodales eleifend.</p><b>Mara Quill</b><small>Marketing Manager</small></div>
      <div class="review" style="left:407px;top:73px"><div class="stars">★★★★★</div><p>Sed placerat convallis aenean fermentum. Aliquet eget feugiat sed consectetur sodales eleifend.</p><b>Tessa Rowan</b><small>Marketing Manager</small></div>
      <div class="review" style="left:292px;top:160px"><div class="stars">★★★★★</div><p>Sed placerat convallis aenean fermentum. Aliquet eget feugiat sed consectetur sodales eleifend.</p><b>Joan Pell</b><small>Marketing Manager</small></div>
      <div class="review" style="left:407px;top:160px"><div class="stars">★★★★★</div><p>Sed placerat convallis aenean fermentum. Aliquet eget feugiat sed consectetur sodales eleifend.</p><b>Owen Brisk</b><small>Marketing Manager</small></div>
    </section>

    <footer class="footer" style="top:1516px;height:180px">
      <div class="ft" style="left:65px;top:36px">Meridale Work Agency Ltd.</div>
      <p class="f" style="left:65px;top:55px;width:135px;font-size:5.5px">Penatibus congue ipsum condimentum ac dignissim non mi auctor. Nulla id id non enim venenatis nibh. Nunc erat morbi auctor.</p>
      <div class="social"><i></i><i></i><i></i><i></i></div>
      <div class="ft" style="left:312px;top:36px;font-weight:400;font-size:8px">Contact</div>
      <p class="f" style="left:312px;top:56px">Toronto, Vancouver,<br>Calgary</p>
      <p class="f" style="left:312px;top:82px">1-888-555-0142</p>
      <p class="f" style="left:312px;top:95px">support@meridalework.com</p>
      <p class="f" style="left:422px;top:36px;line-height:20px">Home<br>About Us<br>Services<br>Events</p>
      <p class="f" style="left:473px;top:36px;line-height:20px">Customer Support<br>How It Works<br>Terms &amp; Condition<br>Privacy Policy</p>
      <div class="rule"></div>
      <div class="copy">© Meridale Work Agency Ltd. | All rights reserved 2024</div>
    </footer>
  </main>

</div>
</body>
</html>
```